Brochure

I have a current booklet for Cedar Ridge Labs, I need to incorporate additional information and testing into it. attached are the current inside pages and the additional items that need to be added.

Requirements
Must have
• matching the background, colors, and format of the original inside booklet pages.

```html
<!DOCTYPE html>
<html lang="en">
<head>
<meta charset="utf-8">
<title>Cedar Ridge Labs – Inside Pages</title>
<link href="https://fonts.googleapis.com/css2?family=Source+Sans+3:wght@400;600;700&display=swap" rel="stylesheet">
<style>
  :root {
    --canvas-bg: #c9c9c9;
    --page-bg: #ffffff;
    --sidebar: #333333;
    --title-blue: #1e6fb9;
    --accent-blue: #1d72bd;
    --panel-blue: #5298d8;
    --panel-text: #eef5fc;
    --body-text: #3f3f3f;
    --band-dark: #4a4a4a;
    --band-light: #8fc0ea;
  }
  * { box-sizing: border-box; margin: 0; padding: 0; }
  html, body { width: 1200px; height: 4880px; overflow: hidden; }
  body {
    background: var(--canvas-bg);
    font-family: "Source Sans 3", "Myriad Pro", Arial, sans-serif;
    color: var(--body-text);
    position: relative;
  }
  .page {
    position: absolute;
    left: 144px;
    width: 923px;
    height: 1130px;
    background: var(--page-bg);
    overflow: hidden;
  }
  .page--1 { top: 125px; }
  .page--2 { top: 1300px; }
  .page--3 { top: 2476px; }
  .page--4 { top: 3606px; }

  .page-art { position: absolute; inset: 0; width: 923px; height: 1130px; }

  .sidebar {
    position: absolute; top: 0; width: 51px; height: 1130px;
    background: var(--sidebar);
    display: flex; align-items: center; justify-content: center;
  }
  .sidebar--left { left: 0; }
  .sidebar--right { right: 0; }
  .sidebar__label {
    color: #fff; font-size: 15px; writing-mode: vertical-rl; white-space: nowrap;
  }
  .sidebar--left .sidebar__label { transform: rotate(180deg); }

  .content { position: absolute; top: 138px; }
  .page--1 .content, .page--3 .content { left: 205px; }
  .page--2 .content { left: 125px; }
  .page--4 .content { left: 140px; top: 142px; }

  .title {
    color: var(--title-blue); font-weight: 400; font-size: 43px;
    letter-spacing: 0.3px; line-height: 1; margin-bottom: 22px;
  }
  .features { list-style: none; margin-left: 6px; }
  .features li {
    font-size: 15px; line-height: 28.5px; padding-left: 20px; position: relative;
  }
  .features li::before {
    content: ""; position: absolute; left: 0; top: 11px;
    width: 7px; height: 7px; border: 1.6px solid var(--accent-blue); border-radius: 50%;
  }
  .features b { font-weight: 700; color: #2b2b2b; }

  .targets {
    color: var(--accent-blue); font-weight: 700; font-size: 21px;
    letter-spacing: 0.6px; margin: 28px 0 16px 12px;
  }
  .intro { font-size: 14.5px; line-height: 22px; margin-left: 12px; width: 620px; }

  .panel {
    position: absolute; background: var(--panel-blue); color: var(--panel-text);
    padding: 36px 36px; display: flex;
  }
  .panel__col { flex: none; }
  .panel__head {
    color: #fff; font-size: 15px; font-weight: 600; text-transform: uppercase; line-height: 24px;
  }
  .panel__head--mixed { text-transform: none; }
  .panel__list { list-style: none; font-size: 14px; }
  .panel__list--loose li { line-height: 25.6px; }
  .panel__list--tight li { line-height: 22.8px; }
  .panel__sub { margin-top: 16px; }

  .page--1 .panel { left: 199px; top: 464px; width: 328px; height: 402px; }
  .page--2 .panel { left: 137px; top: 466px; width: 487px; height: 400px; }
  .page--2 .panel__col:first-child { width: 230px; }
  .page--3 .panel { left: 199px; top: 463px; width: 480px; height: 549px; padding-top: 26px; }
  .page--3 .panel__col:first-child { width: 256px; }
  .page--4 .panel { left: 137px; top: 468px; width: 557px; height: 537px; padding-top: 26px; }
  .page--4 .panel__col:first-child { width: 260px; }

  .page-number { position: absolute; color: #fff; font-size: 13px; }
  .page--1 .page-number, .page--3 .page-number { left: 82px; top: 1072px; }
  .page--2 .page-number, .page--4 .page-number { left: 830px; top: 1074px; color: #e6e6e6; }
</style>
</head>
<body>

<!-- Page 1 -->
<section class="page page--1">
  <svg class="page-art" viewBox="0 0 923 1130" aria-hidden="true">
    <defs>
      <linearGradient id="polyLeft" x1="0" y1="0" x2="1" y2="1">
        <stop offset="0" stop-color="#1e3a66"/><stop offset="0.5" stop-color="#3c78b8"/><stop offset="1" stop-color="#8dc0ec"/>
      </linearGradient>
    </defs>
    <polygon points="51,786 51,1060 230,1060" fill="url(#polyLeft)" role="img" aria-label="Low-poly blue facet decoration"/>
    <polygon points="51,1044 923,1124 923,1130 51,1130" fill="#e6e6e6"/>
    <polygon points="51,1050 900,1130 51,1130" fill="var(--accent-blue)"/>
  </svg>
  <aside class="sidebar sidebar--left"><span class="sidebar__label">Antibiotic Resistance Gene</span></aside>
  <div class="content">
    <h1 class="title">ANTIBIOTIC RESISTANCE GENE</h1>
    <ul class="features">
      <li><b>Cost effective</b> to help maximize your lab’s <b>profits</b></li>
      <li><b>&lt;45 minute</b> run time ensures <b>faster</b> turnaround times</li>
      <li>Compatible with <b>ALL PCR MACHINES</b></li>
      <li><b>Highly demanded</b> targets to make your lab <b>more appealing to providers</b></li>
    </ul>
    <h2 class="targets">12 TARGETS</h2>
    <p class="intro">A provider’s #1 priority is their patients. When you bring them more targets, you are providing them better tools for treatment</p>
  </div>
  <div class="panel">
    <div class="panel__col">
      <h3 class="panel__head">ABR</h3>
      <ul class="panel__list panel__list--loose">
        <li>KPC - Carbapenem resistance</li><li>NDM - Carbapenem resistance</li><li>VIM - Carbapenem resistance</li>
        <li>IMP - Carbapenem resistance</li><li>qnr - Quinolone resistance</li><li>vanB - Vancomycin resistance</li>
        <li>OXA - 48 - Carbapenem resistance</li><li>mecA/mecC - Methicillin resistance</li><li>CTX - M ESBL</li>
        <li>sul - Sulfonamide resistance</li><li>vanA - Vancomycin resistance</li><li>dfrA - Trimethoprim resistance</li>
      </ul>
    </div>
  </div>
  <span class="page-number">1</span>
</section>

<!-- Page 2 -->
<section class="page page--2">
  <svg class="page-art" viewBox="0 0 923 1130" aria-hidden="true">
    <defs>
      <linearGradient id="polyBottom2" x1="0" y1="0" x2="1" y2="0">
        <stop offset="0" stop-color="#d7eafa"/><stop offset="0.5" stop-color="#7fb6e6"/><stop offset="1" stop-color="#3f7fc0"/>
      </linearGradient>
    </defs>
    <polygon points="0,1130 880,1030 880,1130" fill="url(#polyBottom2)" role="img" aria-label="Low-poly light blue facet band"/>
    <polygon points="417,1130 907,1003 907,1130" fill="var(--band-dark)"/>
  </svg>
  <aside class="sidebar sidebar--right"><span class="sidebar__label">Nail/Fungal</span></aside>
  <div class="content">
    <h1 class="title">NAIL/FUNGAL</h1>
    <ul class="features">
      <li><b>Cost effective</b> to help maximize your lab’s <b>profits</b></li>
      <li><b>&lt;45 minute</b> run time ensures <b>faster</b> turnaround times</li>
      <li>Compatible with <b>ALL PCR MACHINES</b></li>
      <li><b>Highly demanded</b> targets to make your lab <b>more appealing to providers</b></li>
    </ul>
    <h2 class="targets">18 TARGETS</h2>
    <p class="intro">A provider’s #1 priority is their patients. When you bring them more targets, you are providing them better tools for treatment</p>
  </div>
  <div class="panel">
    <div class="panel__col">
      <h3 class="panel__head">Fungi</h3>
      <ul class="panel__list panel__list--loose">
        <li>Microsporum gypseum</li><li>Microsporum canis audouinii</li><li>Trichophyton spp</li><li>Malassezia furfur</li>
        <li>Malassezia sympodialis</li><li>Candida krusei</li><li>Candida albicans</li><li>Candida glabrata</li>
        <li>Candida parapsilosis</li><li>Candida auris</li><li>Aspergillus niger</li>
      </ul>
    </div>
    <div class="panel__col">
      <h3 class="panel__head">Fungi</h3>
      <ul class="panel__list panel__list--loose">
        <li>Aspergillus fumigatus</li><li>Aspergillus terreus</li><li>Epidermophyton floccosum</li><li>Fusarium oxysporum</li>
        <li>Trichosporon asahii</li><li>Trichosporon mucoides</li>
      </ul>
    </div>
  </div>
  <span class="page-number">2</span>
</section>

<!-- Page 3 -->
<section class="page page--3">
  <svg class="page-art" viewBox="0 0 923 1130" aria-hidden="true">
    <defs>
      <linearGradient id="polyLeft3" x1="0" y1="0" x2="1" y2="1">
        <stop offset="0" stop-color="#1e3a66"/><stop offset="0.5" stop-color="#3c78b8"/><stop offset="1" stop-color="#8dc0ec"/>
      </linearGradient>
    </defs>
    <polygon points="51,786 51,1060 230,1060" fill="url(#polyLeft3)" role="img" aria-label="Low-poly blue facet decoration"/>
    <polygon points="51,1044 923,1124 923,1130 51,1130" fill="#e6e6e6"/>
    <polygon points="51,1050 900,1130 51,1130" fill="var(--accent-blue)"/>
  </svg>
  <aside class="sidebar sidebar--left"><span class="sidebar__label">Urinary tract infection</span></aside>
  <div class="content">
    <h1 class="title">URINARY TRACT INFECTION</h1>
    <ul class="features">
      <li><b>Cost effective</b> to help maximize your lab’s <b>profits</b></li>
      <li><b>&lt;45 minute</b> run time ensures <b>faster</b> turnaround times</li>
      <li>Compatible with <b>ALL PCR MACHINES</b></li>
      <li><b>Highly demanded</b> targets to make your lab <b>more appealing to providers</b></li>
    </ul>
    <h2 class="targets">28 TARGETS</h2>
    <p class="intro">A provider’s #1 priority is their patients. When you bring them more targets, you are providing them better tools for treatment</p>
  </div>
  <div class="panel">
    <div class="panel__col">
      <h3 class="panel__head">Bacteria</h3>
      <ul class="panel__list panel__list--tight">
        <li>Escherichia coli</li><li>Streptococcus agalactiae</li><li>Klebsiella oxytoca</li><li>Staphylococcus saprophyticus</li>
        <li>Serratia marcescens</li><li>Proteus mirabilis</li><li>Aerococcus urinae</li><li>Treponema pallidum</li>
        <li>Enterobacter cloacae</li><li>Pseudomonas aeruginosa</li><li>Citrobacter freundii</li><li>Klebsiella aerogenes</li>
        <li>Klebsiella pneumoniae</li><li>Morganella morganii</li><li>Corynebacterium urealyticum</li><li>Enterococcus faecium</li>
        <li>Enterococcus faecalis</li><li>Acinetobacter baumannii</li><li>Proteus vulgaris</li><li>Staphylococcus aureus</li>
        <li>Ureplasma</li><li>Providencia satuarti</li>
      </ul>
    </div>
    <div class="panel__col">
      <h3 class="panel__head panel__head--mixed">Fungi</h3>
      <ul class="panel__list panel__list--tight">
        <li>Candida parapsilosis</li><li>Candida glabrata</li><li>Candida auris</li><li>Candida tropicalis</li>
        <li>Candida krusei</li><li>Candida albicans</li>
      </ul>
    </div>
  </div>
  <span class="page-number">3</span>
</section>

<!-- Page 4 -->
<section class="page page--4">
  <svg class="page-art" viewBox="0 0 923 1130" aria-hidden="true">
    <defs>
      <linearGradient id="polyBottom4" x1="0" y1="0" x2="1" y2="0">
        <stop offset="0" stop-color="#d7eafa"/><stop offset="0.5" stop-color="#7fb6e6"/><stop offset="1" stop-color="#3f7fc0"/>
      </linearGradient>
    </defs>
    <polygon points="0,1130 880,1030 880,1130" fill="url(#polyBottom4)" role="img" aria-label="Low-poly light blue facet band"/>
    <polygon points="417,1130 907,1003 907,1130" fill="var(--band-dark)"/>
  </svg>
  <aside class="sidebar sidebar--right"><span class="sidebar__label">Wound/Sepsis</span></aside>
  <div class="content">
    <h1 class="title">WOUND/SEPSIS</h1>
    <ul class="features">
      <li><b>Cost effective</b> to help maximize your lab’s <b>profits</b></li>
      <li><b>&lt;45 minute</b> run time ensures <b>faster</b> turnaround times</li>
      <li>Compatible with <b>ALL PCR MACHINES</b></li>
      <li><b>Highly demanded</b> targets to make your lab <b>more appealing to providers</b></li>
    </ul>
    <h2 class="targets">28 TARGETS</h2>
    <p class="intro">A provider’s #1 priority is their patients. When you bring them more targets, you are providing them better tools for treatment</p>
  </div>
  <div class="panel">
    <div class="panel__col">
      <h3 class="panel__head">Bacteria</h3>
      <ul class="panel__list panel__list--loose">
        <li>Escherichia coli</li><li>Streptococcus agalactiae</li><li>Klebsiella oxytoca</li><li>Staphylococcus saprophyticus</li>
        <li>Pseudomonas aeruginosa</li><li>Staphylococcus haemolyticus</li><li>Enterococcus faecium</li><li>Enterococcus faecalis</li>
        <li>Acinetobacter calcoaceticus</li><li>baumannii complex</li><li>Klebsiella aerogenes</li><li>Klebsiella pneumoniae</li>
        <li>Staphylococcus aureus</li><li>Streptococcus pyogenes</li><li>Streptococcus pneumoniae</li><li>Streptococcus dysgalactise</li>
        <li>Staphylococcus lugdunensis</li><li>Staphylococcus epidermidis</li>
      </ul>
    </div>
    <div class="panel__col">
      <h3 class="panel__head">Fungi</h3>
      <ul class="panel__list panel__list--tight">
        <li>Candida krusei</li><li>Candida tropicals</li><li>Candida glabrata</li><li>Candida parapsilosis</li>
        <li>Candida albicans</li><li>Fusarium solani</li><li>Microsporum spp</li><li>Trichophyton spp</li>
      </ul>
      <h3 class="panel__head panel__sub">Antimic robialresistance</h3>
      <ul class="panel__list panel__list--tight"><li>Methicillin Resistance (MecA+C)</li></ul>
      <h3 class="panel__head panel__head--mixed panel__sub">Viruses</h3>
      <ul class="panel__list panel__list--tight"><li>Herpes Simplex Virus 1</li><li>Herpes Simplex Virus 2</li></ul>
    </div>
  </div>
  <span class="page-number">4</span>
</section>

</body>
</html>
```